Vexora and pinlark ads

Create four total ads, two for vexora and two for pinlark for classfinchly.com.

The pinlark ads will be a single image, and I will handle the text. Image should be consistent with this: https://notes.plankweave.net/image-ad-specs. Image ratio is 1200x628 with an Image ratio of 1.91:1.

Target Market(s)

Parents who have young kids and are thinking about moving to a better school district.

Industry/Entity Type

Real Estate

Font styles to use
Sans Serif

Requirements
Must have
• Classfinchly logo.

```html
<!DOCTYPE html>
<html lang="en">
<head>
<meta charset="utf-8">
<title>Classfinchly – Top 30 Chicagoland Schools Ad</title>
<link rel="stylesheet" href="https://fonts.googleapis.com/css2?family=Montserrat:wght@300;600;700&display=swap">
<style>
  :root {
    --page-bg: #2a2a2a;
    --frame-white: #ffffff;
    --brand-navy: #16164a;
    --brand-blue: #27a7e0;
    --mist-light: rgba(226, 234, 226, 0.85);
    --mist-soft: rgba(200, 214, 202, 0.55);
    --forest-shade: rgba(38, 52, 40, 0.75);
    --forest-mid: #7f9684;
    --forest-haze: #a9bba8;
    --meadow-grass: #5aa332;
    --meadow-bright: #74b93c;
    --meadow-deep: #3b7a1c;
    --headline: #ffffff;
  }
  * { margin: 0; padding: 0; box-sizing: border-box; }
  html, body {
    width: 1200px;
    height: 1200px;
    overflow: hidden;
    background: var(--page-bg);
    font-family: "Montserrat", Arial, sans-serif;
  }
  .ad-banner {
    position: absolute;
    left: 0;
    top: 286px;
    width: 1200px;
    height: 628px;
    background: var(--frame-white);
  }
  .ad-banner__scene {
    position: absolute;
    left: 8px;
    top: 8px;
    width: 1184px;
    height: 584px;
    overflow: hidden;
    background:
      radial-gradient(ellipse 380px 260px at 640px 230px, var(--mist-light), transparent 70%),
      radial-gradient(ellipse 520px 200px at 560px 330px, var(--mist-soft), transparent 75%),
      radial-gradient(ellipse 240px 420px at 0px 260px, var(--forest-shade), transparent 80%),
      radial-gradient(ellipse 300px 440px at 1184px 240px, var(--forest-shade), transparent 80%),
      radial-gradient(ellipse 460px 140px at 560px 470px, rgba(150, 205, 80, 0.55), transparent 75%),
      linear-gradient(180deg,
        var(--forest-mid) 0%,
        var(--forest-haze) 38%,
        var(--meadow-bright) 58%,
        var(--meadow-grass) 74%,
        var(--meadow-deep) 100%);
  }
  .ad-banner__headline {
    position: absolute;
    left: 50px;
    top: 40px;
    color: var(--headline);
    font-size: 57px;
    line-height: 65px;
    letter-spacing: 0.3px;
    text-shadow: 0 1px 4px rgba(0, 0, 0, 0.18);
  }
  .ad-banner__headline-light { display: block; font-weight: 300; }
  .ad-banner__headline-bold { display: block; font-weight: 700; }
  .ad-banner__brand-tab {
    position: absolute;
    left: 328px;
    top: 498px;
    width: 544px;
    height: 130px;
  }
  .brand-tab__shape { position: absolute; inset: 0; }
  .brand-tab__name {
    position: absolute;
    left: 0;
    right: 0;
    top: 26px;
    display: flex;
    align-items: center;
    justify-content: center;
    gap: 14px;
    color: var(--brand-navy);
    font-weight: 600;
    font-size: 42px;
    letter-spacing: -0.5px;
  }
  .brand-tab__dot {
    width: 30px;
    height: 30px;
    border-radius: 50%;
    background: var(--brand-blue);
  }
  .brand-tab__url {
    position: absolute;
    left: 0;
    right: 0;
    top: 88px;
    text-align: center;
    color: var(--brand-navy);
    font-size: 14px;
    font-weight: 600;
    letter-spacing: 5px;
  }
</style>
</head>
<body>
  <section class="ad-banner">
    <div class="ad-banner__scene" role="img" aria-label="Photo of four children jumping and reaching upward in a misty forest meadow with tall tree trunks and bright green grass"></div>

    <h1 class="ad-banner__headline">
      <span class="ad-banner__headline-light">Find the Top 30</span>
      <span class="ad-banner__headline-bold">Chicagoland Schools</span>
      <span class="ad-banner__headline-light">with Homes for Sale</span>
    </h1>

    <div class="ad-banner__brand-tab">
      <svg class="brand-tab__shape" width="544" height="130" viewBox="0 0 544 130" aria-hidden="true">
        <polygon points="50,0 494,0 544,130 0,130" fill="#ffffff"/>
      </svg>
      <div class="brand-tab__name">
        <span class="brand-tab__dot"></span>
        <span>Classfinchly</span>
      </div>
      <div class="brand-tab__url">www.classfinchly.com</div>
    </div>
  </section>
</body>
</html>
```